Design some Business Cards for Bluquartz

We require two professional and creative business cards. Our company is a software and technology company and you can find more info on our website: www.bluquartz.com. You can find our logo files attached.

The final deliverable file has to follow the attached PSD template which is the one our print provider will accept. See the instructions below:

Bleed Area: 88mm x 59mm
Make sure that your background extends to fill the bleed to avoid your Business Cards having white edges when trimmed.

Trim: 84mm x 55mm
This is where we aim to cut the cards.

Safe Area: 80mm x 51mm
Make sure any important aspects of your design such as text and logos are inside of the safe area, otherwise they may be cut off.

To avoid unexpected color changes, edit and save your files in CMYK

Information required on the business card:

Logo (attached)
Name: "Tomas Herrlund"
Job Title: "Technical Director"
Address: "Level 11, 527 Marlow St. Sydney, NSW 2000"
Phone: "+61 2 8317 4625"
email: "tomas@bluquartz.com"
Website: "www.bluquartz.com"

Second business card info (Both business cards are identical. Only difference is name and email )

Name: "Dariusz Koltoneva"
email: "dariusz@bluquartz.com"

```html
<!DOCTYPE html>
<html lang="en">
<head>
<meta charset="utf-8">
<title>Bluquartz Business Card</title>
<link rel="stylesheet" href="https://fonts.googleapis.com/css2?family=Open+Sans:wght@400;600;700&display=swap">
<style>
  :root {
    --stage: #2b2b2b;
    --paper: #ffffff;
    --ink: #1e1e1e;
    --ink-soft: #3a3a3a;
    --brand-red: #c4161c;
    --brand-red-dark: #8e0f13;
    --back-black: #050505;
  }
  * { margin: 0; padding: 0; box-sizing: border-box; }
  html, body {
    width: 1200px; height: 752px; overflow: hidden;
    background: var(--stage);
    font-family: "Open Sans", Arial, sans-serif;
  }
  .stage { position: relative; width: 1200px; height: 752px; }
  .artwork { position: absolute; inset: 0; }

  .front-content, .back-content {
    position: absolute; inset: 0;
    white-space: nowrap;
  }

  .wordmark {
    position: absolute;
    display: flex; align-items: center; gap: 10px;
    font-weight: 700; letter-spacing: 0.5px; line-height: 1;
  }
  .wordmark-dot {
    width: 22px; height: 22px; border-radius: 50%;
    background: var(--brand-red);
  }
  .front-wordmark { left: 107px; top: 272px; font-size: 36px; color: var(--ink); }
  .back-wordmark { right: 125px; top: 437px; font-size: 31px; color: var(--brand-red); }
  .back-wordmark .wordmark-dot { width: 20px; height: 20px; }

  .back-url {
    position: absolute; right: 125px; top: 472px;
    font-size: 12px; line-height: 1; color: var(--brand-red);
  }

  .person-name {
    position: absolute; left: 107px; top: 362px;
    font-size: 16px; line-height: 20px; font-weight: 700; color: var(--ink);
  }
  .person-title {
    position: absolute; left: 107px; top: 383px;
    font-size: 13.5px; line-height: 18px; color: var(--brand-red);
  }
  .contact-list {
    position: absolute; left: 107px; top: 411px;
    list-style: none; font-size: 12.5px; color: var(--ink-soft); line-height: 17.7px;
  }
  .contact-list li { display: flex; align-items: center; gap: 7px; }
  .contact-list .icon { width: 11px; height: 11px; flex: none; }
</style>
</head>
<body>
<div class="stage">
  <svg class="artwork" width="1200" height="752" viewBox="0 0 1200 752" aria-hidden="true">
    <defs>
      <radialGradient id="disc-fill" cx="0.45" cy="0.5" r="0.6">
        <stop offset="0" stop-color="#e03a2a"/>
        <stop offset="0.6" stop-color="#c4161c"/>
        <stop offset="1" stop-color="#8e0f13"/>
      </radialGradient>
      <filter id="disc-shadow" x="-20%" y="-20%" width="140%" height="140%">
        <feDropShadow dx="0" dy="0" stdDeviation="5" flood-color="#000" flood-opacity="0.35"/>
      </filter>
    </defs>
    <rect class="card-front" x="85" y="232" width="507" height="288" fill="#ffffff"/>
    <rect class="card-back" x="608" y="232" width="507" height="288" fill="#050505"/>
    <path class="edge-marker" d="M85 362 a8 8 0 0 1 0 16 z" fill="#c4161c"/>
    <g class="split-disc" filter="url(#disc-shadow)">
      <circle cx="600" cy="376" r="149" fill="#ffffff"/>
      <circle cx="600" cy="376" r="137" fill="url(#disc-fill)"/>
    </g>
    <rect class="card-gap" x="592" y="220" width="16" height="312" fill="#2b2b2b"/>
  </svg>

  <div class="front-content">
    <div class="wordmark front-wordmark"><span>Bluquartz</span><span class="wordmark-dot"></span></div>
    <div class="person-name">Tomas Herrlund</div>
    <div class="person-title">Technical Director</div>
    <ul class="contact-list">
      <li>Level 11, 527 Marlow St. Sydney,</li>
      <li>NSW 2000</li>
      <li>
        <svg class="icon" viewBox="0 0 12 12"><path d="M1 4 Q6 0 11 4 L9.5 5.5 L8 4.2 L4 4.2 L2.5 5.5 Z M3 6 H9 L10 10.5 H2 Z" fill="#c4161c"/></svg>
        <span>+61 2 8317 4625</span>
      </li>
      <li>
        <svg class="icon" viewBox="0 0 12 12"><rect x="1" y="2.5" width="10" height="7" fill="#c4161c"/><path d="M1 2.8 L6 6.5 L11 2.8" stroke="#fff" stroke-width="1" fill="none"/></svg>
        <span>tomas@bluquartz.com</span>
      </li>
      <li>
        <svg class="icon" viewBox="0 0 12 12"><circle cx="6" cy="6" r="5" fill="#c4161c"/><path d="M1 6 H11 M6 1 V11 M6 1 Q3 6 6 11 M6 1 Q9 6 6 11" stroke="#fff" stroke-width="0.7" fill="none"/></svg>
        <span>www.bluquartz.com</span>
      </li>
    </ul>
  </div>

  <div class="back-content">
    <div class="wordmark back-wordmark"><span>Bluquartz</span><span class="wordmark-dot"></span></div>
    <div class="back-url">www.bluquartz.com</div>
  </div>
</div>
</body>
</html>
```